Creative Stationary for Solo Law Firm

I am looking for stationary designs for my solo law firm called TM Halvorsen Law PLLC. My logo is attached. I'd like the logo incorporated into the design.

I'm looking for a stationary design that is a bit outside of the box and not too standard or boring. The final design should communicate professionalism.

Target Market(s)

United States Clients, Opposing Counsel

Industry/Entity Type

Legal

Font styles to use
Sans Serif

Requirements
Must have
• The stationary design must incorporate my logo design attached. The design itself must be creative. The envelope design must follow standard United States designs with room for the postage stamp at the top right corner and space for the recipient's address in the middle.

```html
<!DOCTYPE html>
<html lang="en">
<head>
<meta charset="utf-8">
<title>TM Halvorsen Law PLLC — Stationery</title>
<link rel="stylesheet" href="https://fonts.googleapis.com/css2?family=Montserrat:wght@400;500;600&display=swap">
<style>
  :root{
    --navy:#263475;
    --navy-deep:#1d2860;
    --navy-soft:#3a4889;
    --paper:#ffffff;
    --ink:#4a4d57;
    --ink-light:#8a8d96;
    --stage:#eceef1;
  }
  *{margin:0;padding:0;box-sizing:border-box}
  html,body{width:1200px;height:2700px;overflow:hidden;background:var(--stage)}
  body{position:relative;font-family:"Montserrat",sans-serif;color:var(--ink)}
  .sheet{position:absolute;background:var(--paper);box-shadow:0 6px 18px rgba(20,28,60,.12);overflow:hidden}
  .shape{position:absolute;left:0;width:100%}
  .firm-name{font-family:"Montserrat",sans-serif;font-weight:500;color:var(--navy);letter-spacing:0;white-space:nowrap}
  .firm-name.on-navy{color:#fff}
  .rule{position:absolute;height:2px;background:var(--navy)}
  .contact{position:absolute;font-size:9px;line-height:1.55;color:var(--ink-light);letter-spacing:.02em}

  /* Letterhead */
  .letterhead{left:80px;top:90px;width:500px;height:707px}
  .letterhead .firm-name{position:absolute;left:44px;top:48px;font-size:19px}
  .letterhead .rule{left:44px;right:0;top:82px}
  .letter-body{position:absolute;left:44px;right:44px;top:130px;font-size:9.5px;line-height:1.75;color:var(--ink)}
  .letter-body p{margin-bottom:12px}
  .letter-sign{margin-top:22px}
  .letter-sign strong{display:block;font-weight:600;color:var(--navy)}
  .letterhead .shape{bottom:0;height:70px}
  .letterhead .contact{left:44px;bottom:80px}

  /* Folder */
  .folder{left:620px;top:90px;width:500px;height:707px;background:var(--navy)}
  .folder .shape{bottom:0;height:260px}
  .folder .firm-name{position:absolute;left:0;right:0;top:332px;text-align:center;font-size:28px}

  /* Envelope */
  .envelope{left:80px;top:887px;width:1040px;height:520px}
  .envelope .firm-name{position:absolute;left:56px;top:56px;font-size:24px}
  .envelope .rule{left:56px;width:520px;top:98px}
  .envelope .contact{left:56px;top:116px;font-size:11px}
  .stamp-area{position:absolute;right:56px;top:46px;width:92px;height:108px;border:1.5px dashed #c9ccd6}
  .envelope .shape{bottom:0;height:150px}

  /* Business cards */
  .card{left:200px;width:800px;height:457px}
  .card-front{top:1497px}
  .card-front .person{position:absolute;left:64px;top:64px}
  .card-front .person-name{font-size:34px;font-weight:500;color:var(--navy)}
  .card-front .person-title{font-size:15px;color:var(--ink-light);margin-top:6px;letter-spacing:.06em}
  .card-front .rule{left:64px;width:300px;top:160px}
  .card-front .contact{left:64px;top:190px;font-size:15px;line-height:1.7;color:var(--ink)}
  .card-front .shape{bottom:0;height:110px}
  .card-back{top:2044px;background:var(--navy)}
  .card-back .shape{bottom:0;height:180px}
  .card-back .firm-name{position:absolute;left:0;right:0;top:200px;text-align:center;font-size:38px}
</style>
</head>
<body>

<section class="sheet letterhead">
  <div class="firm-name">TM Halvorsen Law PLLC</div>
  <div class="rule"></div>
  <div class="letter-body">
    <p>Dear Mr. Lindqvist,</p>
    <p>Thank you for meeting with our office last week. We have reviewed the documents you provided and prepared a short summary of the options available to you under current state law.</p>
    <p>Please review the enclosed materials at your convenience. Should you have any questions, do not hesitate to contact us by phone or email, and we will respond promptly.</p>
    <p>We look forward to working with you on this matter and to reaching a fair resolution.</p>
    <div class="letter-sign">Sincerely,<strong>Daniel Reyes</strong>Attorney at Law</div>
  </div>
  <div class="contact">1420 Harbor Lane, Suite 200 · Portland, OR 97201<br>(503) 555-0148 · office@tmhalvorsenlaw.com</div>
  <svg class="shape" viewBox="0 0 500 70" preserveAspectRatio="none" aria-hidden="true">
    <polygon points="0,52 500,40 500,70 0,70" fill="var(--navy-soft)"/>
    <polygon points="180,70 500,14 500,70" fill="var(--navy)"/>
  </svg>
</section>

<section class="sheet folder">
  <svg class="shape" viewBox="0 0 500 260" preserveAspectRatio="none" aria-hidden="true">
    <polygon points="0,260 500,60 500,260" fill="var(--navy-deep)"/>
  </svg>
  <div class="firm-name on-navy">TM Halvorsen Law PLLC</div>
</section>

<section class="sheet envelope">
  <div class="firm-name">TM Halvorsen Law PLLC</div>
  <div class="rule"></div>
  <div class="contact">1420 Harbor Lane, Suite 200<br>Portland, OR 97201<br>(503) 555-0148 · office@tmhalvorsenlaw.com</div>
  <div class="stamp-area"></div>
  <svg class="shape" viewBox="0 0 1040 150" preserveAspectRatio="none" aria-hidden="true">
    <polygon points="0,20 420,150 0,150" fill="var(--navy)"/>
    <polygon points="1040,110 1040,150 760,150" fill="var(--navy-soft)"/>
  </svg>
</section>

<section class="sheet card card-front">
  <div class="person">
    <div class="person-name">Daniel Reyes</div>
    <div class="person-title">Attorney at Law</div>
  </div>
  <div class="rule"></div>
  <div class="contact">(503) 555-0148<br>office@tmhalvorsenlaw.com<br>1420 Harbor Lane, Suite 200, Portland, OR 97201</div>
  <svg class="shape" viewBox="0 0 800 110" preserveAspectRatio="none" aria-hidden="true">
    <polygon points="0,86 800,60 800,110 0,110" fill="var(--navy-soft)"/>
    <polygon points="300,110 800,20 800,110" fill="var(--navy)"/>
  </svg>
</section>

<section class="sheet card card-back">
  <svg class="shape" viewBox="0 0 800 180" preserveAspectRatio="none" aria-hidden="true">
    <polygon points="0,180 800,40 800,180" fill="var(--navy-deep)"/>
  </svg>
  <div class="firm-name on-navy">TM Halvorsen Law PLLC</div>
</section>

</body>
</html>
```